Stationery for Family Law Attorney
Business Cards, Envelope, Letterhead
Stationery for Family Law Attorney - Law
Creative Brief
Professional
Marisol K. Denby
Attorney & Counselor at Law
27815 E. Halvorsen Lane Suite 300 San Diego, CA 92984
marisol@counseldenby.example
Exclusively Family Law www.counseldenby.example
MDenby MDenby
Please note the address should read as follows, on the following lines: Line 1: The Quillgate Line 2: 27815 E. Halvorsen Lane Line 3: Suite 610 Line 4: San Diego, CA 92984
Please note the "San Diego, CA 92984" needs to all be on the same line. (858) 555-0147 is the fax line - not the cell. Also, please add the words "The Quillgate" on the line above the 27815 E. Halvorsen Lane line.
Vektor Vektor
sir please check you inbox top right side this web page
Re #37: Please make the back gray. Please replace the symbols with the words for the contact information (i.e. "Phone"). Please remove the website from the front.
Re #30: Please make the "Marisol K. Denby" and "Attorney & Counselor at Law part in small and large caps. Please remove the website from the front of the card. Instead of letters, please write out "Phone" "Fax" and "Email". Thanks. I really like the gray back of the card.

```html
<!DOCTYPE html>
<html lang="en">
<head>
<meta charset="utf-8">
<title>Marisol K. Denby – Business Cards</title>
<link rel="stylesheet" href="https://fonts.googleapis.com/css2?family=Cinzel:wght@400;600&display=swap">
<style>
  :root {
    --page: #ffffff;
    --card-border: #c9c9c9;
    --blue-light: #3fc3ee;
    --blue-mid: #1ea3d6;
    --blue-deep: #0a78a8;
    --slate: #5e6b75;
    --ink: #3a4650;
    --gray-light: #7b7b7b;
    --gray-dark: #444444;
    --white: #ffffff;
    --swoosh: #8c959c;
  }
  * { margin: 0; padding: 0; box-sizing: border-box; }
  html, body { width: 1200px; height: 706px; overflow: hidden; background: var(--page); }
  body { position: relative; font-family: "Cinzel", "Times New Roman", serif; }

  .card { position: absolute; width: 562px; height: 322px; overflow: hidden; }
  .card--front { left: 24px; top: 24px; background: var(--white); border: 1px solid var(--card-border); }
  .card--back-blue { left: 614px; top: 24px; background: linear-gradient(180deg, var(--blue-mid) 0%, var(--blue-deep) 100%); }
  .card--back-white { left: 24px; top: 362px; background: var(--white); border: 1px solid var(--card-border); }
  .card--back-gray { left: 614px; top: 362px; background: linear-gradient(180deg, var(--gray-light) 0%, var(--gray-dark) 100%); }

  .wave { position: absolute; inset: 0; width: 100%; height: 100%; }

  .wordmark { display: flex; align-items: center; gap: 12px; font-weight: 600; font-size: 22px; letter-spacing: 1px; }
  .wordmark__square { width: 26px; height: 26px; flex: none; }
  .wordmark--front { position: absolute; left: 30px; top: 28px; color: var(--slate); font-size: 19px; }
  .wordmark--front .wordmark__square { background: var(--slate); width: 22px; height: 22px; }

  .back-layout { position: absolute; inset: 0; display: flex; flex-direction: column; align-items: center; }
  .back-layout .wordmark { margin-top: 104px; }
  .url { position: absolute; bottom: 58px; width: 100%; text-align: center; font-size: 15px; letter-spacing: 0.5px; }

  .on-dark { color: var(--white); }
  .on-dark .wordmark__square { background: var(--white); }
  .on-light { color: var(--ink); }
  .on-light .wordmark__square { background: var(--ink); }

  .identity { position: absolute; left: 150px; top: 126px; text-align: center; width: 300px; }
  .identity__name { color: var(--blue-mid); font-size: 22px; line-height: 28px; letter-spacing: 0.5px; }
  .identity__title { color: var(--slate); font-size: 13px; line-height: 18px; margin-top: 2px; }

  .contact { position: absolute; left: 30px; top: 236px; color: var(--white); font-size: 13.5px; line-height: 19px; letter-spacing: 0.3px; font-style: normal; }
</style>
</head>
<body>

<section class="card card--front">
  <svg class="wave" viewBox="0 0 562 322" preserveAspectRatio="none" aria-hidden="true">
    <defs>
      <linearGradient id="frontBlue" x1="0" y1="0" x2="1" y2="0">
        <stop offset="0" stop-color="#0f88bd"/>
        <stop offset="1" stop-color="#3fc3ee"/>
      </linearGradient>
    </defs>
    <path d="M0 206 C 220 228, 430 214, 562 100 L562 322 L0 322 Z" fill="var(--swoosh)"/>
    <path d="M0 214 C 220 236, 430 222, 562 110 L562 322 L0 322 Z" fill="url(#frontBlue)"/>
  </svg>
  <div class="wordmark wordmark--front"><span class="wordmark__square"></span>Marisol K. Denby</div>
  <div class="identity">
    <p class="identity__name">Marisol K. Denby</p>
    <p class="identity__title">Attorney &amp; Counselor at Law</p>
  </div>
  <address class="contact">
    27815 E. Halvorsen Lane<br>
    Suite 610, San Diego, CA 92984<br>
    Phone: (858) 555-0132 | Fax: (858) 555-0147<br>
    Email: marisol@counseldenby.example
  </address>
</section>

<section class="card card--back-blue on-dark">
  <div class="back-layout">
    <div class="wordmark"><span class="wordmark__square"></span>Marisol K. Denby</div>
    <p class="url">www.counseldenby.example</p>
  </div>
</section>

<section class="card card--back-white on-light">
  <div class="back-layout">
    <div class="wordmark"><span class="wordmark__square"></span>Marisol K. Denby</div>
    <p class="url">www.counseldenby.example</p>
  </div>
</section>

<section class="card card--back-gray on-dark">
  <div class="back-layout">
    <div class="wordmark"><span class="wordmark__square"></span>Marisol K. Denby</div>
    <p class="url">www.counseldenby.example</p>
  </div>
</section>

</body>
</html>
```